Tradeon Cup Championship Webdesign project

We need a webdesign for the project called Tradeon. Tradeon™ is an international Forex trading competition to see who can make the most profit in two weeks with all players getting an equal starting sum. Participation is free with no strings attached and the prize money is real, with a total prize pool of $50,000! At the moment Tradeon vol. 2 is about to get launched and we would like to have a new design. On the new website traders should be able to create their own competitions, as well as to invite each other for the cometition.
Updates

Requirements
Must have
• http://www.tradeoncup-example.com/ please refer to this website for the further details.

The website should also include the competition section where traders can invite each other for the competition. It should work similarly to poker competitions.

```html
<!DOCTYPE html>
<html lang="en">
<head>
<meta charset="utf-8">
<title>Tradeon Cup Championship — Intro</title>
<link rel="stylesheet" href="https://fonts.googleapis.com/css2?family=Arimo:wght@400;700&display=swap">
<style>
  :root {
    --sky-top: #7c9fd6;
    --sky-bottom: #35a4dd;
    --blush: #c786b8;
    --deep-blue: #0a6ebd;
    --url-gold: #e0a85a;
    --title-gold: #e7ba7c;
    --count-light: #d3e6ee;
    --count-num: #bfe3f0;
    --bar: #c3d7d4;
    --ghost: rgba(255,255,255,0.22);
  }
  * { margin: 0; padding: 0; box-sizing: border-box; }
  html, body { width: 1200px; height: 779px; overflow: hidden; }
  body { font-family: "Arimo", Arial, sans-serif; background: var(--sky-bottom); }
  .intro-stage { position: relative; width: 1200px; height: 779px; overflow: hidden; }
  .backdrop { position: absolute; inset: 0; }
  .site-url {
    position: absolute; left: 18px; top: 16px;
    font-size: 17px; color: var(--url-gold);
  }
  .countdown {
    position: absolute; left: 439px; top: 46px; width: 322px;
    text-align: center; color: var(--count-light);
  }
  .countdown-label { font-size: 20px; font-weight: 700; letter-spacing: 0.5px; }
  .countdown-timer { font-size: 31px; color: var(--count-num); margin-top: 2px; }
  .countdown-timer b { font-weight: 700; }
  .countdown-timer span { font-weight: 400; font-size: 28px; }
  .countdown-bar {
    height: 16px; background: var(--bar); margin-top: 6px;
    border-radius: 0 0 10px 10px;
  }
  .skip-intro {
    display: inline-block; margin-top: 6px;
    font-size: 19px; font-weight: 700; color: var(--count-light); text-decoration: none;
  }
  .tagline { position: absolute; white-space: nowrap; font-weight: 400; }
  .tagline-ghost { color: var(--ghost); }
  .tagline-ghost.g1 { left: 30px; top: 322px; font-size: 28px; }
  .tagline-ghost.g2 { left: 44px; top: 340px; font-size: 32px; }
  .tagline-ghost.g3 { left: 82px; top: 358px; font-size: 37px; }
  .tagline-main { left: 116px; top: 382px; font-size: 41px; color: var(--title-gold); }
</style>
</head>
<body>
<main class="intro-stage">
  <svg class="backdrop" width="1200" height="779" viewBox="0 0 1200 779" aria-hidden="false">
    <defs>
      <linearGradient id="sky" x1="0" y1="0" x2="0" y2="1">
        <stop offset="0" stop-color="var(--sky-top)"/>
        <stop offset="1" stop-color="var(--sky-bottom)"/>
      </linearGradient>
      <radialGradient id="blush" cx="1200" cy="0" r="700" gradientUnits="userSpaceOnUse">
        <stop offset="0" stop-color="var(--blush)"/>
        <stop offset="1" stop-color="var(--blush)" stop-opacity="0"/>
      </radialGradient>
      <linearGradient id="flagTone" x1="0" y1="0" x2="0" y2="1">
        <stop offset="0" stop-color="#ffffff" stop-opacity="0.12"/>
        <stop offset="0.5" stop-color="#d9e6f0" stop-opacity="0.22"/>
        <stop offset="1" stop-color="#ffffff" stop-opacity="0.12"/>
      </linearGradient>
      <linearGradient id="ribbon" x1="0" y1="0" x2="1" y2="0">
        <stop offset="0" stop-color="#ffffff" stop-opacity="0"/>
        <stop offset="0.5" stop-color="#ffffff" stop-opacity="0.16"/>
        <stop offset="1" stop-color="#ffffff" stop-opacity="0"/>
      </linearGradient>
    </defs>
    <rect class="sky" width="1200" height="779" fill="url(#sky)"/>
    <rect class="blush-glow" width="1200" height="779" fill="url(#blush)"/>
    <path class="deep-wave" fill="var(--deep-blue)"
      d="M0,0 H1168 C1185,150 1120,330 950,425 C830,490 700,500 600,497 C420,490 170,390 0,318 Z"/>
    <g class="flag-columns" role="img" aria-label="Columns of faded national flags of the competing countries">
      <rect x="36" y="236" width="70" height="490" fill="url(#flagTone)"/>
      <rect x="204" y="88" width="72" height="640" fill="url(#flagTone)"/>
      <rect x="402" y="156" width="64" height="560" fill="url(#flagTone)"/>
      <rect x="566" y="224" width="66" height="496" fill="url(#flagTone)"/>
      <rect x="740" y="262" width="72" height="456" fill="url(#flagTone)"/>
      <rect x="910" y="50" width="72" height="672" fill="url(#flagTone)"/>
      <rect x="1086" y="262" width="76" height="460" fill="url(#flagTone)"/>
    </g>
    <g class="light-ribbons" role="img" aria-label="Sweeping ribbons of thin white lines">
      <path d="M80,290 C300,120 700,160 1200,170 L1200,200 C700,210 320,170 90,300 Z" fill="url(#ribbon)"/>
      <path d="M40,680 C300,560 700,520 1200,600 L1200,630 C700,560 320,600 60,700 Z" fill="url(#ribbon)"/>
    </g>
  </svg>

  <a class="site-url" href="#">http://www.tradeoncup-example.com/</a>

  <section class="countdown">
    <div class="countdown-label">LIVE! &nbsp;COUNTDOWN</div>
    <div class="countdown-timer"><b>43</b><span>d</span> <b>23</b><span>h</span> <b>21</b><span>m</span> <b>40</b><span>s</span></div>
    <div class="countdown-bar"></div>
    <a class="skip-intro" href="#">skip intro</a>
  </section>

  <h1 class="tagline tagline-ghost g1" aria-hidden="true">THE CHALLENGE CONTINUES</h1>
  <div class="tagline tagline-ghost g2" aria-hidden="true">THE CHALLENGE CONTINUES</div>
  <div class="tagline tagline-ghost g3" aria-hidden="true">THE CHALLENGE CONTINUES</div>
  <div class="tagline tagline-main">THE CHALLENGE CONTINUES...</div>
</main>
</body>
</html>
```